ALL TYPES OF COMMERCIAL PLASTERING

TYPE OF BLOCK LETTERING WITH STAND OUT QUALITIES
WITH SOME TYPE OF LOGO
SOMETHING UNIQUE FOR THE BUILDING INDUSTRY.
QUALITY WORKMANSHIP
Updates

forgot to include my mobile phone number on my brief. could you add it to your design please MOBILE PH 0418 695 031

please let me make this quite clear ,the company name is northgate linings and Fitouts PTY LTD. THE TYPE OF WORK WE WILL BE DOING IS COMMERCIAL PLASTERING.

Industry/Entity Type

Industry

Contact Information for Business Card

northgate linings and fitouts P/L
martin corbell p.o.box 42 wendouree 3355 email address northgatelinings@mailbox-example.com
ABN 51 847 213 906 COMMERCIAL PLASTERING

```html
<!DOCTYPE html>
<html lang="en">
<head>
<meta charset="utf-8">
<title>Northgate Linings and Fitouts — Business Card</title>
<link rel="stylesheet" href="https://fonts.googleapis.com/css2?family=Bebas+Neue&family=Open+Sans:wght@400;600;800&display=swap">
<style>
  :root {
    --backdrop: #9a9a9a;
    --card-white: #ffffff;
    --ink: #111111;
    --orange: #f28c1c;
    --orange-deep: #e0661f;
    --silver-light: #e6e6e6;
    --silver-dark: #8c8c8c;
    --panel-top: #2a2a2a;
    --panel-bottom: #0d0d0d;
    --divider: #9a9a9a;
    --contact-text: #ffffff;
  }
  * { box-sizing: border-box; margin: 0; padding: 0; }
  html, body {
    width: 1200px;
    height: 900px;
    overflow: hidden;
    background: var(--backdrop);
  }
  .canvas {
    position: relative;
    width: 1200px;
    height: 900px;
  }
  .business-card {
    position: absolute;
    left: 100px;
    top: 170px;
    width: 1000px;
    height: 560px;
    border-radius: 30px;
    overflow: hidden;
    background: var(--card-white);
    box-shadow: 0 18px 40px rgba(0,0,0,0.28);
  }
  .card-top {
    position: absolute;
    left: 0; top: 0;
    width: 100%;
    height: 300px;
    background: var(--card-white);
  }
  .brand-mark {
    position: absolute;
    left: 0; right: 0;
    top: 62px;
    display: flex;
    justify-content: center;
    align-items: center;
    gap: 18px;
  }
  .brand-square {
    width: 58px;
    height: 58px;
    background: var(--orange);
  }
  .brand-word {
    font-family: 'Bebas Neue', sans-serif;
    font-size: 96px;
    line-height: 1;
    color: var(--orange);
    letter-spacing: 2px;
  }
  .company-name {
    position: absolute;
    left: 0; right: 0;
    top: 218px;
    text-align: center;
    font-family: 'Bebas Neue', sans-serif;
    font-size: 62px;
    line-height: 1;
    color: var(--ink);
    letter-spacing: 0.5px;
  }
  .silver-rule {
    position: absolute;
    left: 0; top: 296px;
    width: 100%;
    height: 7px;
    background: linear-gradient(180deg, var(--silver-light), var(--silver-dark));
  }
  .tagline-band {
    position: absolute;
    left: 0; top: 303px;
    width: 100%;
    height: 32px;
    background: var(--orange);
    display: flex;
    align-items: center;
    justify-content: center;
  }
  .tagline {
    font-family: 'Open Sans', sans-serif;
    font-weight: 800;
    font-size: 18px;
    letter-spacing: 0.62em;
    color: var(--ink);
    padding-left: 0.62em;
  }
  .card-bottom {
    position: absolute;
    left: 0; top: 335px;
    width: 100%;
    height: 225px;
    background: linear-gradient(180deg, var(--panel-top), var(--panel-bottom));
  }
  .holder-name {
    position: absolute;
    left: 60px;
    width: 400px;
    top: 84px;
    text-align: right;
    font-family: 'Open Sans', sans-serif;
    font-weight: 600;
    font-size: 36px;
    color: var(--orange);
    letter-spacing: 0.5px;
  }
  .divider {
    position: absolute;
    left: 500px;
    top: 34px;
    width: 2px;
    height: 160px;
    background: var(--divider);
  }
  .contact-list {
    position: absolute;
    left: 528px;
    top: 38px;
    list-style: none;
    font-family: 'Open Sans', sans-serif;
    font-size: 23px;
    color: var(--contact-text);
    line-height: 1;
  }
  .contact-item {
    display: flex;
    align-items: center;
    height: 34px;
  }
  .contact-icon {
    width: 26px;
    height: 26px;
    margin-right: 8px;
    flex: none;
  }
  .contact-item.no-icon { padding-left: 34px; }
</style>
</head>
<body>
<main class="canvas">
  <article class="business-card">
    <section class="card-top">
      <div class="brand-mark">
        <span class="brand-square"></span>
        <span class="brand-word">NORTHGATE</span>
      </div>
      <h1 class="company-name">NORTHGATE LININGS AND FITOUTS PTY LTD</h1>
    </section>
    <div class="silver-rule"></div>
    <div class="tagline-band">
      <p class="tagline">ALL TYPES OF COMMERCIAL PLASTERING</p>
    </div>
    <section class="card-bottom">
      <h2 class="holder-name">MARTIN CORBELL</h2>
      <div class="divider"></div>
      <ul class="contact-list">
        <li class="contact-item">
          <svg class="contact-icon" viewBox="0 0 26 26" aria-hidden="true">
            <rect x="7" y="2" width="12" height="22" rx="2" fill="var(--orange)"/>
            <rect x="9" y="5" width="8" height="7" fill="#1a1a1a"/>
            <g fill="#1a1a1a">
              <rect x="9" y="14" width="2" height="2"/><rect x="12" y="14" width="2" height="2"/><rect x="15" y="14" width="2" height="2"/>
              <rect x="9" y="17" width="2" height="2"/><rect x="12" y="17" width="2" height="2"/><rect x="15" y="17" width="2" height="2"/>
              <rect x="9" y="20" width="2" height="2"/><rect x="12" y="20" width="2" height="2"/><rect x="15" y="20" width="2" height="2"/>
            </g>
          </svg>
          0418 695 031
        </li>
        <li class="contact-item">
          <svg class="contact-icon" viewBox="0 0 26 26" aria-hidden="true">
            <path d="M13 3 L25 14 L21 14 L21 24 L15 24 L15 18 L11 18 L11 24 L5 24 L5 14 L1 14 Z" fill="var(--orange)"/>
          </svg>
          p.o.box 42 wendouree 3355
        </li>
        <li class="contact-item">
          <svg class="contact-icon" viewBox="0 0 26 26" aria-hidden="true">
            <rect x="2" y="7" width="22" height="15" rx="1.5" fill="var(--orange)"/>
            <path d="M2 8 L13 16 L24 8" fill="none" stroke="#1a1a1a" stroke-width="1.8"/>
          </svg>
          northgatelinings@mailbox-example.com
        </li>
        <li class="contact-item no-icon">ABN 51 847 213 906</li>
      </ul>
    </section>
  </article>
</main>
</body>
</html>
```